Flayer & Brochure Design for Moving and Logistics company

Brochure for offices and B2B. We are targeting Furniture Manufactures, and Furniture Companies. We offer delivery service from the manufacturer to the furniture store, and from the store to the consumer. We also offer the ability to store the furniture and assemble it.

Website: https://www.brevantor.com/

Target Market(s)

B2B (furniture / staging/ design companies)

Industry/Entity Type

Logistics/ moving/ delivery

Font styles to use
Sans Serif

Colors
0054AA
0677BA
7BADD7
CADEEF
E8F1F8
0094D4
00A9DD
6FCCEA
C7EBF8
E9F6FB

```html
<!DOCTYPE html>
<html lang="en">
<head>
<meta charset="utf-8">
<title>Brevantor Trifold Brochure</title>
<link rel="stylesheet" href="https://fonts.googleapis.com/css2?family=Roboto:wght@500;700;900&family=Source+Sans+3:wght@400;600;700&display=swap">
<style>
:root{
  --navy:#26339a;
  --royal:#0054aa;
  --panel-blue:#1e48ad;
  --sky:#0094d4;
  --cyan:#00a9dd;
  --light-cyan:#6fccea;
  --pale:#e8f1f8;
  --paper:#ffffff;
  --ink:#2b2b33;
  --backdrop:#b9babd;
}
*{box-sizing:border-box;margin:0;padding:0}
html,body{width:742px;height:1200px;overflow:hidden;background:var(--backdrop)}
body{position:relative;font-family:"Source Sans 3",Arial,sans-serif;color:var(--ink)}
.spread{position:absolute;left:46px;width:663px;height:514px;background:var(--paper);overflow:hidden;box-shadow:0 8px 10px rgba(0,0,0,.18)}
.spread--outside{top:58px}
.spread--inside{top:632px}
.panel{position:absolute;top:0;height:100%;overflow:hidden}
.panel--left{left:0;width:216px;background:linear-gradient(180deg,#fff 40%,#eef0f3)}
.panel--middle{left:216px;width:219px;background:var(--panel-blue)}
.panel--right{left:435px;width:228px;background:linear-gradient(180deg,#fff,#f3f4f6)}
.photo{position:absolute}
.abs{position:absolute}
.heading{font-family:"Roboto",Arial,sans-serif;font-weight:700;color:var(--navy);text-transform:uppercase;letter-spacing:.1px}
.rule{position:absolute;height:2px;background:var(--navy)}
.body-copy{font-size:8.6px;line-height:1.27;text-align:justify}
.body-copy p+p{margin-top:8px}
.wordmark{font-family:"Roboto",Arial,sans-serif;font-weight:500;letter-spacing:-.5px}
.pill{position:absolute;background:var(--panel-blue);color:#fff;border-radius:10px;display:flex;align-items:center;justify-content:center;gap:5px;font-family:"Roboto",Arial,sans-serif;font-weight:700}
.team-name{font-size:9.6px;font-weight:700;color:var(--light-cyan)}
.team-mail{font-size:9.6px;color:#fff;display:flex;align-items:center;gap:4px;margin-top:1px}
.contact-line{font-size:10px;color:#333;text-align:center;width:100%}
.service{position:absolute;left:14px;display:flex;align-items:center;gap:9px;font-size:8.8px;line-height:1.15;color:#333}
.service-icon{width:20px;height:20px;border-radius:4px;background:var(--navy);flex:none}
.sub{font-size:8.4px;font-weight:600;color:var(--light-cyan);text-align:center}
.white-copy{color:#fff}
</style>
</head>
<body>

<!-- Outside spread -->
<section class="spread spread--outside">
  <div class="panel panel--left">
    <div class="photo" role="img" aria-label="Two movers in uniforms carrying a white sofa past stacked cardboard boxes" style="left:0;top:0;width:216px;height:230px;background:linear-gradient(160deg,#d9d6d0,#a9a49b 55%,#5f6f96);clip-path:polygon(0 0,100% 0,100% 84%,0 100%)"></div>
    <svg class="abs" style="left:0;top:150px" width="216" height="140" viewBox="0 0 216 140">
      <polygon points="0,40 150,125 0,120" fill="var(--cyan)"/>
      <polygon points="216,60 216,135 120,140 150,125" fill="var(--panel-blue)"/>
    </svg>
    <h2 class="heading abs" style="left:14px;top:258px;font-size:13px">Who we are</h2>
    <div class="rule" style="left:14px;top:281px;width:90px"></div>
    <div class="body-copy abs" style="left:14px;top:293px;width:188px">
      <p>In a world that's changing fast, companies have to be empathetic, efficient—and elastic. So we don't do just one thing, we do many.</p>
      <p>We can move you from A to B, hang your curtains, install your appliances and assemble your furniture. Apartments, mansions, freight, storage, logistics.</p>
      <p>We make it easier » and cheaper » to get things done for your home and business.</p>
    </div>
    <svg class="abs" style="left:0;top:476px" width="216" height="12"><rect y="2" width="216" height="3" fill="var(--panel-blue)"/><rect y="8" width="216" height="1.5" fill="var(--panel-blue)"/></svg>
  </div>

  <div class="panel panel--middle">
    <svg class="abs" style="left:0;top:0" width="219" height="514" viewBox="0 0 219 514">
      <polygon points="0,395 219,430 219,514 0,514" fill="#ffffff"/>
      <polygon points="0,380 219,418 219,430 0,395" fill="#e9f6fb" opacity=".35"/>
    </svg>
    <div class="wordmark abs" style="left:0;width:219px;top:42px;text-align:center;font-size:38px;color:#fff">brevantor</div>
    <h3 class="heading abs" style="left:0;width:219px;text-align:center;top:101px;font-size:12.5px;color:var(--light-cyan)">Our team:</h3>
    <div class="abs" style="left:40px;top:127px">
      <div class="team-name">Marlon Dessaint</div>
      <div class="team-mail"><svg width="8" height="8"><circle cx="4" cy="4" r="4" fill="#fff"/><rect x="2" y="2.7" width="4" height="2.6" fill="var(--panel-blue)"/></svg>Marlon@brevantor.com</div>
      <div class="team-name" style="margin-top:11px">Grant Holloway</div>
      <div class="team-mail"><svg width="8" height="8"><circle cx="4" cy="4" r="4" fill="#fff"/><rect x="2" y="2.7" width="4" height="2.6" fill="var(--panel-blue)"/></svg>Grant@brevantor.com</div>
      <div class="team-name" style="margin-top:11px">Nadia Korvalis</div>
      <div class="team-mail"><svg width="8" height="8"><circle cx="4" cy="4" r="4" fill="#fff"/><rect x="2" y="2.7" width="4" height="2.6" fill="var(--panel-blue)"/></svg>Nadia@brevantor.com</div>
    </div>
    <div class="abs" style="left:49px;top:270px;width:122px;height:122px;border-radius:50%;background:var(--cyan);padding:6px">
      <div role="img" aria-label="Long corridor of blue storage unit doors" style="width:100%;height:100%;border-radius:50%;border:3px solid #fff;background:radial-gradient(circle,#dfe8ef 10%,#7f9fbd 60%,#42668f)"></div>
    </div>
    <div class="abs" style="left:0;top:402px;width:219px">
      <div class="contact-line">www.brevantor.com</div>
      <div class="contact-line">info@brevantor.com</div>
    </div>
    <div class="pill" style="left:34px;top:435px;width:151px;height:20px;font-size:12px">
      <svg width="12" height="12" viewBox="0 0 12 12"><circle cx="6" cy="6" r="6" fill="#fff"/><path d="M3.6 3.2l1.2-.4.7 1.6-.7.6c.4.8 1 1.4 1.8 1.8l.6-.7 1.6.7-.4 1.2c-2.6.1-4.9-2.2-4.8-4.8z" fill="var(--panel-blue)"/></svg>
      555 210 3864
    </div>
    <div class="contact-line abs" style="top:461px;font-size:9.6px">48 Harbor Row, Brooklyn, NY 11200</div>
    <svg class="abs" style="left:0;top:476px" width="219" height="12"><rect y="2" width="219" height="3" fill="var(--panel-blue)"/><rect y="8" width="219" height="1.5" fill="var(--panel-blue)"/></svg>
  </div>

  <div class="panel panel--right">
    <div class="photo" role="img" aria-label="Smiling family with two children playing in a cardboard moving box" style="left:0;top:0;width:228px;height:370px;background:linear-gradient(170deg,#ece9e4,#c9b9a6 55%,#a98a6a);clip-path:polygon(0 0,100% 0,100% 66%,0 100%)"></div>
    <svg class="abs" style="left:0;top:230px" width="228" height="160" viewBox="0 0 228 160">
      <polygon points="0,140 228,15 228,40 0,160" fill="var(--panel-blue)"/>
      <polygon points="228,40 228,110 90,110" fill="var(--cyan)"/>
    </svg>
    <div class="wordmark abs" style="left:0;width:228px;top:372px;text-align:center;font-size:40px;color:var(--panel-blue)">brevantor</div>
    <h1 class="heading abs" style="left:0;width:228px;top:424px;text-align:center;font-size:23px;line-height:1.12;color:var(--panel-blue)">For people on<br>the move</h1>
    <svg class="abs" style="left:0;top:476px" width="228" height="12"><rect y="2" width="228" height="3" fill="var(--panel-blue)"/><rect y="8" width="228" height="1.5" fill="var(--panel-blue)"/></svg>
    <div class="pill" style="left:45px;top:485px;width:140px;height:18px;font-size:10px">
      <svg width="9" height="9" viewBox="0 0 10 10"><circle cx="5" cy="5" r="4.3" fill="none" stroke="#fff" stroke-width="1"/><path d="M.7 5h8.6M5 .7c-2.4 2.4-2.4 6.2 0 8.6M5 .7c2.4 2.4 2.4 6.2 0 8.6" fill="none" stroke="#fff" stroke-width=".8"/></svg>
      www.brevantor.com
    </div>
  </div>
</section>

<!-- Inside spread -->
<section class="spread spread--inside">
  <div class="panel panel--left">
    <div class="photo" role="img" aria-label="Young couple sitting on the floor among moving boxes" style="left:0;top:0;width:216px;height:230px;background:linear-gradient(150deg,#e8ddd0,#c19a76 50%,#6d86b5);clip-path:polygon(0 0,100% 0,100% 70%,0 100%)"></div>
    <svg class="abs" style="left:0;top:150px" width="216" height="100" viewBox="0 0 216 100">
      <polygon points="216,0 216,60 120,50" fill="var(--cyan)"/>
    </svg>
    <div class="photo" role="img" aria-label="Open cardboard boxes stacked together" style="left:92px;top:155px;width:110px;height:70px;background:linear-gradient(160deg,#e0b98b,#b9895a)"></div>
    <h2 class="heading abs" style="left:14px;top:235px;font-size:13px">Our services:</h2>
    <div class="rule" style="left:14px;top:255px;width:188px;height:1px;opacity:.5"></div>
    <div class="service" style="top:271px"><span class="service-icon"></span>Residential &amp; Commercial Moving</div>
    <div class="service" style="top:301px"><span class="service-icon"></span>Supplies and/or Packing / Furniture<br>Delivery &amp; Dis/Assembly</div>
    <div class="service" style="top:337px"><span class="service-icon"></span>Warehousing &amp; Storage /<br>Home &amp; Business Projects</div>
    <div class="service" style="top:367px"><span class="service-icon"></span>Rubbish &amp; Recycling / Freight Delivery</div>
    <svg class="abs" style="left:22px;top:412px" width="70" height="102" viewBox="0 0 70 102"><circle cx="35" cy="35" r="31" fill="none" stroke="var(--panel-blue)" stroke-width="6"/></svg>
    <div class="heading abs" style="left:113px;top:412px;font-size:15px;line-height:1.25;text-transform:none;color:var(--navy)">Zerro<br>Worries</div>
    <div class="abs" style="left:113px;top:454px;font-size:9px;color:var(--sky)">Get your quote on</div>
    <div class="pill" style="left:109px;top:469px;width:100px;height:14px;font-size:8.8px">
      <svg width="8" height="8" viewBox="0 0 10 10"><circle cx="5" cy="5" r="4.3" fill="none" stroke="#fff" stroke-width="1"/><path d="M.7 5h8.6M5 .7c-2.4 2.4-2.4 6.2 0 8.6M5 .7c2.4 2.4 2.4 6.2 0 8.6" fill="none" stroke="#fff" stroke-width=".8"/></svg>
      www.brevantor.com
    </div>
  </div>

  <div class="panel panel--middle">
    <svg class="abs" style="left:0;top:76px" width="219" height="8"><rect width="219" height="2.5" fill="#fff"/></svg>
    <h2 class="heading abs" style="left:0;width:219px;top:120px;text-align:center;font-size:13px;color:#fff">Residential moving</h2>
    <div class="sub abs" style="left:0;width:219px;top:147px">Go with less stress to your next address.</div>
    <div class="body-copy white-copy abs" style="left:14px;top:163px;width:191px">
      <p>Whether you're a natural minimalist or have decades of possessions, we have the expertise, methods and materials to make moving easier. We don't ask why you have 256 unopened boxes of super hero action figures, we just move them.</p>
      <p>We've seamlessly completed hundreds of moves for residents all over NYC, Tri-State area and beyond. Our fleet includes trucks and sprinter vans, balancing our ability to maneuver as NYC movers and also carry serious loads.</p>
      <p>Our vehicles meet the most modern emission standards, we have relationships with recycling facilities appropriate to all waste removal jobs, and we utilize as many reusable materials as possible.</p>
    </div>
    <h2 class="heading abs" style="left:0;width:219px;top:368px;text-align:center;font-size:13px;color:#fff">Supplies &amp; packing</h2>
    <div class="sub abs" style="left:0;width:219px;top:396px">Many hands make light work.</div>
    <div class="body-copy white-copy abs" style="left:14px;top:412px;width:191px">
      <p>Boxes, bins, bubble wrap, muscle. We can pack up a residence or a business with care—and can even work while you watch remotely. We can dump or donate what you don't want to take with you, put items in storage, pack your fragile belongings with utmost care and professionally wrap furniture.</p>
    </div>
  </div>

  <div class="panel panel--right">
    <h2 class="heading abs" style="left:19px;top:29px;font-size:13px;line-height:1.35">Furniture delivery &amp;<br>dis/ assembly</h2>
    <div class="abs" style="left:19px;top:79px;font-size:8.4px;font-weight:600;color:var(--sky)">All together and under wraps.</div>
    <div class="body-copy abs" style="left:19px;top:96px;width:191px">
      <p>We have extensive experience delivering and assembling furniture, for everyone from apartment stagers to government agencies to high-end manufacturers and makers. We treat all items as if they were our own.</p>
      <p>You'll see us bubble wrapping sharp corners, taking care to organize hardware and more. All goods are strapped securely in vehicles, delivered with care, unwrapped and assembled upon arrival. We are the top partner to furniture rental companies and deliver and assemble furniture all day every day.</p>
      <p>When it comes to NYC abodes, we've seen it all. Like ultra-narrow apartment doors, tight garden-level vestibules, low-hanging overhead storage solutions and much more. Taking doors off the hinges and legs off tables is par for the course.</p>
    </div>
    <div class="photo" role="img" aria-label="Office room with a wrapped chair and stacked moving boxes" style="left:0;top:345px;width:228px;height:169px;background:linear-gradient(180deg,#f4f4f2,#d8c8b2 60%,#b59066);clip-path:polygon(0 12%,100% 0,100% 100%,0 100%)"></div>
    <svg class="abs" style="left:0;top:320px" width="228" height="110" viewBox="0 0 228 110">
      <polygon points="228,0 228,75 150,60" fill="var(--cyan)"/>
    </svg>
  </div>
</section>

</body>
</html>
```